Yummy Mummy Flyer

Flyer that will be handed and also appear in magazine advertisements.

The campaign is aimed women that want to get pregnant, are pregnant or are post pregnancy. We are a private one-to-one pilates studio and will tailor packages to suit individual client's needs.

We want the colour scheme to be consistent to the website: www.delphinewarrickpilates.com We want the overall theme to exude exclusivity as our target market is the affluent upper middle class in Kensington and Chelsea, London
Updates

Hi Guys,

Thank you for the questions!
A5 please, one sided, landscape. 
All the best,
Delphine

To All the Designers,

Thank you so much for your submissions so far. I am extremely impressed with all of them! There are bits and pieces of a few designs that I think would look really nice if they were incorporated together. A few of
 the highlights are:
936979- I like this one, but please don't say, 'I am... (Delphine Warrick) please just put, 'Delphine with Talise 5 months'
934981- I really like the layout but not the color scheme on this one. Please put the web address as: www.delphinewarrickpilates.com
928472- This is my favorite design but the wording isn't quite right. 
927155-I like the layout and wording of this one.
931394- I like how, 'The Baby you dreamed of the body you deserve' is written. Please try and incorporate!
927947- I love how the website and studio logo is done. Please try and incorporate!
Thank you so much for all of your hard work and I look forward to seeing more of your submissions..
All the best,
Delphine

Reason: Hi! I am still waiting for the updated versions of the advert since my last comments... please email me if you have any questions... Thank you so much and looking forward to seeing the submissions soon... Delphine

Industry/Entity Type

Tailor

Requirements
Must have
• Incorporate the supplied photo (you can photoshop/alter the image as you see fit)

The picture is the studio owner with her daughter. Caption should read 'Delphine with daughter Talise, 5 months'

The design layout needs to work as both a flyer and as an advertisement in a magazine.

Needs to have website address, phone number (0207 611 3472), slogan 'The baby you dreamed of.....the body you deserve' & 'Whether you are pre or post pregnancy our team tailors programs for all stages'

You are free to suggest your take on how it looks, reads, design layout etc. Artistic freedom granted!
Nice to have
• Please refer to the attached recent press release by my PR agent. Please use any copy you feel necessary.

```html
<!DOCTYPE html>
<html lang="en">
<head>
<meta charset="utf-8">
<title>Delphine Warrick Private Pilates Studio – Flyer</title>
<link rel="stylesheet" href="https://fonts.googleapis.com/css2?family=Cabin:wght@400;500&family=Tinos:ital,wght@0,700;1,400&display=swap">
<style>
  :root {
    --panel-grey: #d6d6d6;
    --brand-purple: #5a3ddc;
    --brand-lilac: #a996e6;
    --band-purple: #5b40e0;
    --white: #ffffff;
    --wall-light: #ece8e0;
    --wall-mid: #d9d2c4;
    --sand: #c8a67a;
  }
  html, body {
    margin: 0;
    padding: 0;
    overflow: hidden;
    background: #ffffff;
  }
  .flyer {
    position: relative;
    width: 1200px;
    height: 856px;
    overflow: hidden;
    background: var(--panel-grey);
    font-family: "Tinos", "Times New Roman", serif;
  }
  .photo {
    position: absolute;
    left: 0;
    top: 0;
    width: 472px;
    height: 856px;
    background: linear-gradient(180deg, var(--wall-light) 0%, var(--wall-mid) 55%, #cdb48e 72%, var(--sand) 100%);
  }
  .photo-caption {
    position: absolute;
    left: 0;
    width: 472px;
    top: 712px;
    margin: 0;
    text-align: center;
    color: var(--white);
    font-style: italic;
    font-weight: 400;
    font-size: 41px;
    line-height: 54px;
  }
  .content {
    position: absolute;
    left: 472px;
    top: 0;
    width: 728px;
    height: 856px;
    text-align: center;
  }
  .content > * {
    white-space: nowrap;
  }
  .studio-name {
    margin: 0;
    position: absolute;
    left: 0;
    right: 0;
    top: 70px;
    font-family: "Cabin", "Gill Sans", sans-serif;
    font-weight: 500;
    font-size: 70px;
    line-height: 84px;
    color: var(--brand-purple);
    letter-spacing: -1px;
  }
  .studio-type {
    margin: 0;
    position: absolute;
    left: 0;
    right: 0;
    top: 166px;
    font-family: "Cabin", "Gill Sans", sans-serif;
    font-weight: 400;
    font-size: 38px;
    line-height: 46px;
    letter-spacing: 3px;
    color: var(--brand-lilac);
  }
  .tagline {
    margin: 0;
    position: absolute;
    left: 0;
    right: 0;
    top: 236px;
    font-weight: 700;
    font-size: 27px;
    line-height: 34px;
    color: var(--brand-purple);
  }
  .stages {
    margin: 0;
    position: absolute;
    left: 0;
    right: 0;
    top: 274px;
    font-style: italic;
    font-weight: 400;
    font-size: 19px;
    line-height: 24px;
    color: var(--brand-purple);
  }
  .slogan {
    margin: 0;
    position: absolute;
    left: 0;
    right: 0;
    top: 312px;
    font-style: italic;
    font-weight: 400;
    font-size: 41px;
    line-height: 52px;
    color: var(--white);
  }
  .sessions {
    margin: 0;
    position: absolute;
    left: 0;
    right: 20px;
    top: 440px;
    font-weight: 700;
    font-size: 30px;
    line-height: 41px;
    color: var(--brand-purple);
  }
  .hours {
    margin: 0;
    position: absolute;
    left: 0;
    right: 0;
    top: 541px;
    font-weight: 700;
    font-size: 30px;
    color: var(--brand-purple);
  }
  .contact-band {
    position: absolute;
    left: 17px;
    top: 615px;
    width: 676px;
    height: 131px;
    background: var(--band-purple);
    color: var(--white);
    font-weight: 700;
  }
  .contact-web {
    margin: 0;
    position: absolute;
    left: 0;
    right: 0;
    top: 12px;
    font-size: 35px;
  }
  .contact-phone {
    margin: 0;
    position: absolute;
    left: 0;
    right: 0;
    top: 54px;
    font-size: 56px;
    line-height: 66px;
  }
  .address {
    margin: 0;
    position: absolute;
    left: 0;
    right: 20px;
    top: 763px;
    font-style: normal;
    font-weight: 700;
    font-size: 20px;
    line-height: 29px;
    color: var(--brand-purple);
  }
</style>
</head>
<body>
  <main class="flyer">
    <div class="photo" role="img" aria-label="Photo of Delphine in a blue bikini and straw sun hat, seen from behind, holding her baby daughter Talise against a sunlit white wall with palm fronds"></div>
    <p class="photo-caption">Delphine with daughter<br>Talise, 5 months</p>

    <section class="content">
      <h1 class="studio-name">DELPHINE WARRICK</h1>
      <p class="studio-type">Private Pilates Studio</p>
      <p class="tagline">Pilates Before, During and After Pregnancy</p>
      <p class="stages">Whether you are pre or post pregnancy our team tailors programs for all stages</p>
      <p class="slogan">'The baby you dreamed of.....<br>the body you deserve'</p>
      <p class="sessions">Sessions are 55 mins and range<br>from £45 - £85 p/hour</p>
      <p class="hours">Opening hours:&nbsp; Mon – Fri, 7am – 9pm</p>
      <div class="contact-band">
        <p class="contact-web">www.delphinewarrickpilates.com</p>
        <p class="contact-phone">0207 611 3472</p>
      </div>
      <address class="address">The Delphine Warrick Private Pilates Studio<br>14 Harrow Mews, London. SW7 9QT</address>
    </section>
  </main>
</body>
</html>
```